Clara Joy Halden- Lantern Waltz- Autumn/Winter Tour Dates

I need high res A3 Tour poster for print and for social media JPG sharing of tour dates.
Also needed Facebook/Twitter Banner Cover Photos of these dates.
Text Needed Below
Clara Joy Halden
Lantern Waltz
Autumn/Winter Tour Dates
03/09 Ravensby Folk Festival
21/09 Swindon- Calder Theatre
01/10 Hitchin- Brackwell Folk Club
17/10 Bath- The Anvil
20/10 Sheffield- Upper Dale Croquet Club
24/10 Birmingham- Orchard Lamp Cafe
26/10 Glasgow- The Nook and Jar
27/10 Edinburgh - The Marble Parlour
08/11 Capital Reel and Ballad Festival- The Crooked Heron
25/11 Lewes- Tandem Record Shop- Live In Store
02/12 Cambridge- The Quayside
27/01 Lincolnshire- Fenmarsh Theatre
Tickets/Info: www.clarajoyhalden-music.example/gigs
(Quotes/Reviews To Put On)
"Outstanding, rich and expressive."            "Vibrant and Experimental"
**** BdM                                                               **** Tunepaths
"Impressive and Invigorating"                        "Enchanting" Acoustic Wire UK
tBarks

Updates
I cannot read the tour dates on most of the submissions so far. They need to be visible to viewers.
Thank You.
Please also be as creative and inventive as possible- not bland.

Target Market(s)
Music Fans- Folk Acoustic Americana
Industry/Entity Type
Media
Font styles to use
Requirements
Must have
- My photo featured prominently
- Look classy and not tacky or OTT
- Look elegant, wintery and eye catching
- The dates must be very clear to read
- Links to Website:

Nice to have
- Something innovative and not boring in terms of layout design
- Perhaps fading/ misty or wintery

Should not have
- Any colours that do not match

```html
<!DOCTYPE html>
<html lang="en">
<head>
<meta charset="utf-8">
<title>Clara Joy Halden – Lantern Waltz – Autumn/Winter Tour Dates</title>
<link rel="stylesheet" href="https://fonts.googleapis.com/css2?family=Lora:wght@500&family=Cinzel:wght@400&family=Montserrat:wght@500;600&family=Allura&display=swap">
<style>
  :root {
    --page-bg: #e2e2e2;
    --night-deep: #070c22;
    --night-mid: #1b2d58;
    --frost: #8ea6c8;
    --mist: #4d6690;
    --band: #0c1a44;
    --title-light: #eef4ff;
    --title-blue: #86aeea;
    --date-blue: #5d9be6;
    --text-white: #ffffff;
    --rule: #8a97b8;
  }
  * { margin: 0; padding: 0; box-sizing: border-box; }
  html, body { width: 1200px; height: 1200px; overflow: hidden; }
  body { background: var(--page-bg); }

  .poster {
    position: absolute; left: 218px; top: 60px;
    width: 765px; height: 1081px;
    background: var(--night-deep);
    overflow: hidden;
  }
  .portrait-area {
    position: absolute; left: 0; top: 0; width: 765px; height: 912px;
    background:
      radial-gradient(ellipse 22% 20% at 50% 36%, rgba(168,186,214,0.75) 0%, rgba(120,144,184,0.4) 55%, transparent 100%),
      radial-gradient(ellipse 40% 45% at 52% 45%, var(--mist) 0%, rgba(52,76,118,0.7) 45%, transparent 100%),
      radial-gradient(ellipse 30% 30% at 90% 70%, rgba(110,135,175,0.45) 0%, transparent 100%),
      radial-gradient(ellipse 35% 40% at 10% 40%, rgba(70,95,140,0.45) 0%, transparent 100%),
      radial-gradient(ellipse 90% 80% at 55% 45%, var(--night-mid) 0%, var(--night-deep) 100%);
  }
  .portrait-area::after {
    content: ""; position: absolute; inset: 0;
    background: linear-gradient(to bottom, rgba(7,12,34,0.6) 0%, transparent 20%, transparent 60%, rgba(7,12,34,0.92) 100%);
  }

  .title-block { position: absolute; top: 28px; width: 100%; text-align: center; }
  .title-block h1, .title-block h2 {
    font-family: "Lora", serif; font-weight: 500; line-height: 70px; letter-spacing: 1px;
    background: linear-gradient(to bottom, var(--title-light) 25%, var(--title-blue) 100%);
    -webkit-background-clip: text; background-clip: text; color: transparent;
  }
  .artist-name { font-size: 58px; }
  .album-name { font-size: 58px; margin-top: 8px; }

  .tour-heading {
    position: absolute; left: 39px; top: 648px; width: 220px;
    text-align: center; font-family: "Cinzel", serif; font-weight: 400;
    font-size: 35px; line-height: 41.5px; color: var(--text-white);
  }

  .tour-dates {
    position: absolute; left: 278px; top: 562px;
    list-style: none; font-family: "Montserrat", sans-serif; font-weight: 600;
    font-size: 17.5px; line-height: 24.8px; color: var(--text-white);
  }
  .tour-dates li { display: flex; }
  .tour-dates .date { color: var(--date-blue); width: 73px; flex: none; }

  .info-band {
    position: absolute; left: 0; top: 912px; width: 765px; height: 144px;
    background: var(--band);
  }
  .tickets {
    position: absolute; left: 37px; top: 966px; width: 390px; height: 37px;
    border-top: 1px solid var(--rule); border-bottom: 1px solid var(--rule);
    font-family: "Montserrat", sans-serif; font-weight: 500; font-size: 13px;
    line-height: 35px; color: var(--text-white); white-space: nowrap;
  }
  .tickets .label { color: var(--date-blue); font-weight: 600; }

  .reviews { position: absolute; left: 453px; top: 927px; list-style: none; }
  .reviews li { height: 28.5px; display: flex; align-items: baseline; gap: 8px; color: var(--text-white); }
  .reviews .quote { font-family: "Allura", cursive; font-size: 20px; }
  .reviews .source { font-family: "Montserrat", sans-serif; font-weight: 500; font-size: 9.5px; color: var(--date-blue); }
</style>
</head>
<body>
  <main class="poster">
    <div class="portrait-area" role="img" aria-label="Portrait photo of the singer in a snowy, misty winter forest, lit in deep frosty blue tones"></div>

    <header class="title-block">
      <h1 class="artist-name">Clara Joy Halden</h1>
      <h2 class="album-name">Lantern Waltz</h2>
    </header>

    <h3 class="tour-heading">Autumn/<br>Winter<br>Tour<br>Dates</h3>

    <ul class="tour-dates">
      <li><span class="date">03/09</span><span>Ravensby Folk Festival</span></li>
      <li><span class="date">21/09</span><span>Swindon- Calder Theatre</span></li>
      <li><span class="date">01/10</span><span>Hitchin- Brackwell Folk Club</span></li>
      <li><span class="date">17/10</span><span>Bath- The Anvil</span></li>
      <li><span class="date">20/10</span><span>Sheffield- Upper Dale Croquet Club</span></li>
      <li><span class="date">24/10</span><span>Birmingham- Orchard Lamp Cafe</span></li>
      <li><span class="date">26/10</span><span>Glasgow- The Nook and Jar</span></li>
      <li><span class="date">27/10</span><span>Edinburgh - The Marble Parlour</span></li>
      <li><span class="date">08/11</span><span>Capital Reel and Ballad Festival-<br>The Crooked Heron</span></li>
      <li><span class="date">25/11</span><span>Lewes- Tandem Record Shop- Live In Store</span></li>
      <li><span class="date">02/12</span><span>Cambridge- The Quayside</span></li>
      <li><span class="date">27/01</span><span>Lincolnshire- Fenmarsh Theatre</span></li>
    </ul>

    <section class="info-band"></section>
    <p class="tickets"><span class="label">Tickets/Info:</span> <span class="url">www.clarajoyhalden-music.example/gigs</span></p>
    <ul class="reviews">
      <li><span class="quote">Vibrant and Experimental</span><span class="source">Tunepaths</span></li>
      <li><span class="quote">Outstanding, Rich and Expressive</span><span class="source">BdM</span></li>
      <li><span class="quote">Impressive and Invigorating</span><span class="source">tBarks</span></li>
      <li><span class="quote">Enchanting</span><span class="source">Acoustic Wire UK</span></li>
    </ul>
  </main>
</body>
</html>
```